Visitenkarte für Ergotherapiepraxis
Zielgruppe
Wir arbeiten mit Kindern und Erwachsene jeden Alters.
Diese Personen kommen mit Beeinträchtigungen (körperlich, seelisch, schulisch) im täglichen Leben zu uns. Wir unterstützen unsere Patienten die Beeinträchtigungen zu verringern oder zu kompensieren und so den Alltag besser bewältigen zu können.
Aufgabenstellung
Ein Design was Kinder und Erwachsene anspricht, aber nicht zu verspielt wirkt. Es soll vertrauenserweckend sein. Eventuell sollte die Visitenkarte ein "aufgehendes oder erblühendes oder aufsteigendes" Element enthalten (=zu Beginn war die Beeinträchtigung dann steigt die Lebensqualität als Folge der Behandlung)
Daten vorn:
Ergotherapiepraxis

```html
<!DOCTYPE html>
<html lang="de">
<head>
<meta charset="utf-8">
<title>Visitenkarte Ergotherapiepraxis</title>
<link rel="stylesheet" href="https://fonts.googleapis.com/css2?family=Barlow:wght@300;400;500;600&display=swap">
<style>
  :root {
    --brand-green: #00963f;
    --brand-red: #990a0a;
    --text-grey: #5b5b5b;
    --ghost-grey: #efefef;
    --paper: #ffffff;
    --address-strip: #fbfbfb;
    --frame-dark: #1a1a1a;
    --frame-light: #bdbdbd;
  }
  * { margin: 0; padding: 0; box-sizing: border-box; }
  html, body { width: 934px; height: 1200px; overflow: hidden; background: var(--paper); }
  body { position: relative; font-family: "Barlow", Arial, sans-serif; }

  .card {
    position: absolute;
    left: 95px;
    width: 709px;
    height: 458px;
    background: var(--paper);
    overflow: hidden;
  }
  .card--front { top: 126px; border: 1px solid var(--frame-dark); }
  .card--back { top: 615px; border: 1.5px solid var(--frame-light); }

  .band { position: absolute; left: 0; right: 0; background: var(--brand-green); }
  .card--front .band--main { top: 291px; height: 103px; }
  .card--front .band--address { top: 394px; height: 44px; background: var(--address-strip); }
  .card--front .band--foot { top: 438px; height: 20px; }
  .card--back .band--main { top: 313px; height: 78px; }

  .brand {
    position: absolute;
    left: 40px;
    top: 120px;
    display: flex;
    align-items: center;
    gap: 12px;
    font-weight: 600;
    font-size: 40px;
    line-height: 1;
    color: var(--brand-green);
  }
  .brand__dot { width: 34px; height: 34px; border-radius: 50%; background: var(--brand-green); }
  .brand--ghost { left: 30px; top: 110px; font-size: 64px; color: var(--ghost-grey); }
  .brand--ghost .brand__dot { width: 56px; height: 56px; background: var(--ghost-grey); }

  .tagline {
    position: absolute;
    left: 44px;
    top: 176px;
    font-size: 15px;
    font-weight: 400;
    line-height: 1;
    color: var(--brand-red);
  }

  .line {
    position: absolute;
    margin: 0;
    line-height: 1;
    white-space: nowrap;
  }
  .divider {
    display: inline-block;
    position: relative;
    width: 2px;
    height: 0.7em;
    vertical-align: baseline;
  }
  .divider::after {
    content: "";
    position: absolute;
    left: 0;
    bottom: -5px;
    width: 2px;
    height: 53px;
    background: var(--brand-green);
  }

  .practice { left: 299px; top: 251px; font-size: 37px; font-weight: 500; }
  .practice__main { color: var(--text-grey); font-weight: 500; }
  .practice .divider { margin: 0 4px 0 3px; }
  .practice__sub { color: var(--brand-red); font-weight: 400; }

  .therapist-name { left: 299px; top: 294px; font-size: 37px; font-weight: 500; color: var(--paper); }
  .phone { left: 297px; top: 363px; font-size: 31px; font-weight: 500; color: var(--paper); }
  .address { left: 44px; top: 404px; font-size: 30px; font-weight: 500; color: var(--brand-red); }

  .therapist-label { left: 302px; top: 282px; font-size: 28px; color: var(--brand-green); }
  .therapist-label__main { font-weight: 600; }
  .therapist-label .divider { margin: 0 5px; }
  .therapist-label__sub { font-weight: 300; }
</style>
</head>
<body>
  <section class="card card--front" aria-label="Vorderseite">
    <div class="band band--main"></div>
    <div class="band band--address"></div>
    <div class="band band--foot"></div>

    <div class="brand"><span class="brand__dot"></span>Wurzelgrund</div>
    <p class="tagline">…für Ihre Lebensqualität</p>

    <h1 class="line practice">
      <span class="practice__main">Ergotherapie</span><span class="divider"></span><span class="practice__sub">praxis</span>
    </h1>
    <p class="line therapist-name">Lene Marwitz</p>
    <p class="line phone">Tel. 033920/48175</p>
    <p class="line address">Lindenweg 4 | 15831 Birkhain, OT Wiesau</p>
  </section>

  <section class="card card--back" aria-label="Rückseite">
    <div class="brand brand--ghost" aria-hidden="true"><span class="brand__dot"></span>Wurzelgrund</div>
    <div class="band band--main"></div>
    <p class="line therapist-label">
      <span class="therapist-label__main">Behandelnder</span><span class="divider"></span><span class="therapist-label__sub">Therapeut/in:</span>
    </p>
  </section>
</body>
</html>
```